Fairway Flare Relief promotional cards (rack card)

This will be an eye catching (rack) card designed to be left at the Golf clubhouse with special event coordinators and emailed or physically handed to charities conducting fund raising golf tournaments. I need an electronic file version that I could email to prospects to view before they decide if they will help promote this to their tournament directors
Photos, logos, files and website link are attached. all photos on my website are available upon request.
www.fairwayflarerelief.example
Target Market(s)
must be appealing to charities conducting golf tournaments as a method to raise funds,
Industry/Entity Type
Golf Course
Font styles to use
Other font styles liked:
- Screwed Oblique for any bold type, serif for body text
Requirements
Must have
- include a call to action to "book your event now"
- use the colors in my logo
- include the photo attached, could include additional photos from my website
- include "several packages to choose from"
- I would like this to be vectorized to be able to resize or shrink slightly as needed to fit printables.
Nice to have
- in the background of photos, there is a 7 foot pull up banner that participants often stand in front of to take videos and photos, you can incorporate that if possible as a watermark or background image. I can provide that original image if needed.
Should not have
- any salesy "car commercial" banners or balloons or stars or anything like that.

```html
<!DOCTYPE html>
<html lang="en">
<head>
<meta charset="utf-8">
<title>Fairway Flare Relief – Rack Card</title>
<link rel="stylesheet" href="https://fonts.googleapis.com/css2?family=Oswald:wght@500;700&family=Open+Sans:wght@400;600;700;800&family=Russo+One&display=swap">
<style>
  :root {
    --green-deep: #0b3a1c;
    --green-mid: #1f6b3a;
    --green-bright: #3f9a5a;
    --green-glow: #8fd39a;
    --orange: #f08a1c;
    --white: #ffffff;
    --banner-white: #eef0ec;
  }
  * { margin: 0; padding: 0; box-sizing: border-box; }
  html, body { width: 924px; height: 1200px; overflow: hidden; }
  body { font-family: "Open Sans", sans-serif; color: var(--white); background: var(--green-deep); }

  .card {
    position: relative; width: 924px; height: 1200px; overflow: hidden;
    background:
      radial-gradient(ellipse 420px 360px at 560px 330px, rgba(143,211,154,.35), transparent 70%),
      radial-gradient(ellipse 300px 260px at 800px 620px, rgba(180,220,180,.28), transparent 70%),
      linear-gradient(180deg, #1d6a3a 0%, #17562f 45%, #124524 70%, #0c3519 100%);
  }
  .background-photo { position: absolute; inset: 0; }

  .pullup-banner {
    position: absolute; left: 28px; top: 30px; width: 258px; height: 588px;
    background: linear-gradient(180deg, var(--banner-white) 0%, #d7e3d5 40%, #8fb48c 65%, #e6ebe3 100%);
    box-shadow: 0 4px 14px rgba(0,0,0,.35);
  }

  .brand-mark {
    position: absolute; right: 36px; top: 20px; text-align: right;
    font-family: "Russo One", sans-serif; font-size: 25px; line-height: 30px; color: var(--white);
    letter-spacing: 1px;
  }
  .brand-url { display: block; margin-top: 8px; font-family: "Open Sans", sans-serif; font-weight: 700; font-size: 11px; letter-spacing: 0; }

  .headline {
    position: absolute; left: 333px; top: 218px; width: 572px;
    font-family: "Oswald", sans-serif; text-transform: uppercase; line-height: 33px;
  }
  .headline .question { color: var(--orange); font-size: 27px; font-weight: 700; }
  .headline .pitch { color: var(--white); font-size: 19px; font-weight: 700; letter-spacing: .3px; }

  .intro { position: absolute; left: 333px; width: 566px; font-size: 16.5px; line-height: 22px; }
  .intro-one { top: 418px; }
  .intro-two { top: 496px; text-align: justify; }

  .packages-band {
    position: absolute; left: 0; top: 592px; width: 924px; height: 258px;
    background: linear-gradient(180deg, rgba(8,40,18,.55), rgba(8,40,18,.35));
  }
  .packages-title {
    position: absolute; left: 36px; top: 624px;
    font-family: "Oswald", sans-serif; font-weight: 700; font-size: 21px; text-transform: uppercase;
  }
  .option {
    position: absolute; top: 668px; width: 205px; height: 148px; border-radius: 50% / 42%;
    background: radial-gradient(ellipse at 50% 55%, rgba(170,230,170,.85) 0%, var(--green-bright) 45%, #0f3a1b 100%);
    text-align: center; padding-top: 18px;
    font-size: 13px; font-weight: 700; line-height: 16px; color: var(--white);
  }
  .option h3 { color: var(--orange); font-size: 16px; font-weight: 700; margin-bottom: 2px; }
  .option p { padding: 0 26px; }
  .opt1 { left: 22px; } .opt2 { left: 252px; } .opt3 { left: 485px; top: 660px; } .opt4 { left: 714px; }
  .opt4 p { padding: 0 34px; }

  .terms { position: absolute; left: 34px; width: 862px; font-size: 13.8px; line-height: 17px; }
  .terms strong { font-family: "Oswald", sans-serif; font-weight: 700; font-size: 19px; text-transform: uppercase; letter-spacing: .3px; }
  .terms-approval { top: 858px; }
  .terms-funds { top: 934px; }

  .call-to-action {
    position: absolute; left: 0; top: 1024px; width: 924px; text-align: center;
    font-family: "Oswald", sans-serif; font-weight: 700; font-size: 46px; color: var(--orange);
  }
  .contact { position: absolute; left: 0; top: 1134px; width: 924px; text-align: center; font-size: 16.5px; line-height: 24px; }
  .contact .sep { margin: 0 22px; }
</style>
</head>
<body>
<main class="card">
  <div class="background-photo" role="img" aria-label="Close-up photo of a gloved golfer's hand placing a ball on a tee above green grass, tinted green"></div>

  <div class="pullup-banner" role="img" aria-label="Photo of the 7 foot pull-up event banner with brand name, silhouette of a shooter on a golf course and hashtag"></div>

  <div class="brand-mark">
    Fairway<br>Flare<br>Relief
    <span class="brand-url">www.fairwayflarerelief.example</span>
  </div>

  <h1 class="headline">
    <span class="question">Are you tired or bored of the same old challenges at every charity golf tournament?</span>
    <span class="pitch">How about adding an exciting alternative to your typical golf tournament fundraising efforts by providing a sporting rifle golf ball launcher.</span>
  </h1>

  <p class="intro intro-one">Mulligans, longest drive, putting contests, Hole In One for a car? Yeah, you've been there and done that! Now it is time to add a new challenge?</p>
  <p class="intro intro-two">We set up on a par 4 or par 5 and your registered players will have the opportunity to use the rifle to launch their golf ball approximately 400 yards in place of driving off a tee.</p>

  <div class="packages-band"></div>
  <h2 class="packages-title">Several packages to choose from</h2>

  <section class="option opt1"><h3>OPTION 1:</h3><p>($250 fee) $5 or $10 per player/per shot (player pays to participate)( player provides a ball)</p></section>
  <section class="option opt2"><h3>OPTION 2:</h3><p>($500 fee sponsor level) $5 or $10 per player/per shot and I provide all players a logo ball) 100% profit to the charity</p></section>
  <section class="option opt3"><h3>OPTION3:</h3><p>($500 fee -sponsor level) player participation is included in mulligan package price. 100% profit to the charity</p></section>
  <section class="option opt4"><h3>OPTION4:</h3><p>Custom package design based upon charity requests</p></section>

  <p class="terms terms-approval"><strong>Approval:</strong> I request that the tournament director and the golf course clubhouse manager both acknowledge that they have approved of the use of the sporting rifle golf ball launcher and are aware of the noise associated with it, and assume all liabilities beyond the teebox as they do for any other promotional event occurring on their course. (Ie- longest drive, hole in one, involving a participant teeing off.)</p>
  <p class="terms terms-funds"><strong>Collecting Funds:</strong> I provide two options for collecting funds. The preferred method is to have players make a donation at the selected hole. The alternative is to accept credit cards via card reader at the hole for players who do not have cash but would like to make a donation anyways. Cash, tickets and card reader totals are turned in after the final foursome fires away!</p>

  <h2 class="call-to-action">BOOK YOUR EVENT NOW</h2>

  <p class="contact">To book your date, please feel free to email me or call me.<br>
    Dana@fairwayflarerelief.example<span class="sep">|</span>555-014-2298<span class="sep">|</span>www.fairwayflarerelief.example</p>
</main>
</body>
</html>
```